Sleek business card design for digital agency.

Brief document attached for detailed description and inspiration. Looking for a minimalist sleek, cool, modern business card design.

Industry/Entity Type

Digital

```html
<!DOCTYPE html>
<html lang="en">
<head>
<meta charset="utf-8">
<title>Ember Labs — Business Card</title>
<link href="https://fonts.googleapis.com/css2?family=Open+Sans:wght@400;600;700&display=swap" rel="stylesheet">
<style>
  :root {
    --stage: #2e2e2e;
    --card: #151515;
    --card-edge: #0c0c0c;
    --emboss: #242424;
    --accent: #2b9fdc;
    --text: #d8d8d8;
    --text-soft: #bdbdbd;
    --faint: #222222;
  }
  * { margin: 0; padding: 0; box-sizing: border-box; }
  html, body { width: 1200px; height: 814px; overflow: hidden; }
  body {
    background: var(--stage);
    font-family: "Open Sans", Arial, sans-serif;
    position: relative;
  }
  .card {
    position: absolute;
    top: 248px;
    width: 520px;
    height: 318px;
    background: var(--card);
    border: 1px solid var(--card-edge);
    border-radius: 3px;
    box-shadow: 0 14px 30px rgba(0,0,0,0.45);
  }
  .card--front { left: 50px; }
  .card--back { left: 630px; }

  .front-mark {
    position: absolute;
    inset: 0;
    display: flex;
    align-items: center;
    justify-content: center;
    gap: 14px;
    color: var(--emboss);
    font-weight: 700;
    font-size: 46px;
    letter-spacing: 0.5px;
  }
  .front-mark__dot {
    width: 26px; height: 26px;
    border-radius: 50%;
    background: var(--emboss);
  }

  .contact-list {
    position: absolute;
    left: 34px;
    top: 34px;
    list-style: none;
  }
  .contact-list li {
    display: flex;
    align-items: center;
    gap: 10px;
    height: 19px;
    font-size: 12.5px;
    color: var(--text);
  }
  .contact-icon {
    width: 13px; height: 13px;
    flex: none;
  }

  .back-mark {
    position: absolute;
    left: 34px;
    top: 176px;
    font-size: 22px;
    font-weight: 700;
    color: var(--faint);
  }

  .address {
    position: absolute;
    left: 34px;
    bottom: 40px;
    font-size: 12.5px;
    line-height: 19px;
    color: var(--text-soft);
  }

  .identity {
    position: absolute;
    right: 36px;
    top: 150px;
    text-align: right;
  }
  .identity__name {
    font-size: 18px;
    font-weight: 700;
    letter-spacing: 1px;
    color: var(--accent);
    text-transform: uppercase;
  }
  .identity__title {
    font-size: 13px;
    color: var(--text);
    margin-top: 2px;
  }
</style>
</head>
<body>

  <section class="card card--front" aria-label="Card front">
    <div class="front-mark">
      <span class="front-mark__dot"></span>
      <span>Ember Labs</span>
    </div>
  </section>

  <section class="card card--back" aria-label="Card back">
    <ul class="contact-list">
      <li>
        <svg class="contact-icon" viewBox="0 0 13 13"><circle cx="6.5" cy="6.5" r="6.5" fill="var(--accent)"/><path d="M4.3 3.4c.4-.3.8-.2 1 .2l.5 1c.1.3 0 .6-.2.8l-.4.3c.3.8.9 1.4 1.7 1.7l.3-.4c.2-.2.5-.3.8-.2l1 .5c.4.2.5.6.2 1-.6.8-1.5.9-2.4.4-1.2-.6-2.2-1.6-2.8-2.8-.4-.9-.3-1.8.3-2.5z" fill="#151515"/></svg>
        0400 218 476
      </li>
      <li>
        <svg class="contact-icon" viewBox="0 0 13 13"><circle cx="6.5" cy="6.5" r="6.5" fill="var(--accent)"/><path d="M4.3 3.4c.4-.3.8-.2 1 .2l.5 1c.1.3 0 .6-.2.8l-.4.3c.3.8.9 1.4 1.7 1.7l.3-.4c.2-.2.5-.3.8-.2l1 .5c.4.2.5.6.2 1-.6.8-1.5.9-2.4.4-1.2-.6-2.2-1.6-2.8-2.8-.4-.9-.3-1.8.3-2.5z" fill="#151515"/></svg>
        03 9120 4488
      </li>
      <li>
        <svg class="contact-icon" viewBox="0 0 13 13"><circle cx="6.5" cy="6.5" r="6.5" fill="var(--accent)"/><rect x="3.3" y="4.2" width="6.4" height="4.6" rx="0.6" fill="#151515"/><path d="M3.6 4.5l2.9 2.2 2.9-2.2" stroke="var(--accent)" stroke-width="0.7" fill="none"/></svg>
        dhartley@emberlabs.com
      </li>
      <li>
        <svg class="contact-icon" viewBox="0 0 13 13"><circle cx="6.5" cy="6.5" r="6.5" fill="var(--accent)"/><circle cx="6.5" cy="6.5" r="3.4" fill="none" stroke="#151515" stroke-width="0.9"/><path d="M3.1 6.5h6.8M6.5 3.1c-1.6 2-1.6 4.8 0 6.8M6.5 3.1c1.6 2 1.6 4.8 0 6.8" stroke="#151515" stroke-width="0.7" fill="none"/></svg>
        www.emberlabs.com
      </li>
      <li>
        <svg class="contact-icon" viewBox="0 0 13 13"><circle cx="6.5" cy="6.5" r="6.5" fill="var(--accent)"/></svg>
        social.com/EmberLabs
      </li>
      <li>
        <svg class="contact-icon" viewBox="0 0 13 13"><circle cx="6.5" cy="6.5" r="6.5" fill="var(--accent)"/></svg>
        @dhartley82
      </li>
    </ul>

    <div class="back-mark">Ember Labs</div>

    <address class="address" style="font-style:normal">
      Level 2, 18 Carver St<br>
      Northbridge NSW 5000
    </address>

    <div class="identity">
      <div class="identity__name">Daniel Hartley</div>
      <div class="identity__title">Marketing Director</div>
    </div>
  </section>

</body>
</html>
```